New LLC consulting company needs a business card design

I need a business card design for new company in Alexandria Virginia called TK Verdane Consulting LLC. The company is focused on consulting for defense and national security issues with expertise in nuclear and space topics. I would like to see designs that are simple and I am open to colors except for brown.

Target Market(s)

All businesses that are seeking consulting help

Industry/Entity Type

Consulting

Contact Information for Business Card

Name of company - TK Verdane Consulting LLC; name (Delia Hartwig) President; email: hartwigdl47@mailnest.example; Phone: 555-862-4197

Requirements
Must have
• The details described above
Nice to have
• I'm open to all ideas
Should not have
• No brown

```html
<!DOCTYPE html>
<html lang="en">
<head>
<meta charset="utf-8">
<title>TK Verdane Consulting LLC – Business Card</title>
<link rel="stylesheet" href="https://fonts.googleapis.com/css2?family=Oswald:wght@700&family=Poppins:wght@400&display=swap">
<style>
  :root {
    --backdrop: #9d9d9d;
    --paper: #ffffff;
    --navy: #1b2a55;
    --royal: #2f58cf;
    --ink: #222222;
    --rule: #c9c9c9;
  }
  * { margin: 0; padding: 0; box-sizing: border-box; }
  html, body {
    width: 1093px; height: 1200px; overflow: hidden;
    background: var(--backdrop);
  }
  .canvas { position: relative; width: 1093px; height: 1200px; }

  .card {
    position: absolute; left: 265px; width: 578px; height: 356px;
    border-radius: 24px; overflow: hidden;
  }
  .card--front { top: 226px; background: var(--paper); }
  .card--back { top: 621px; background: var(--navy); }

  .front__band {
    position: absolute; left: 0; right: 0; bottom: 0; height: 17px;
    background: var(--navy);
  }
  .front__company {
    position: absolute; left: 0; width: 298px; top: 134px;
    font-family: "Oswald", sans-serif; font-weight: 700;
    font-size: 35px; line-height: 40px; text-align: center;
    text-transform: uppercase; color: var(--navy); letter-spacing: -1px;
    white-space: nowrap;
  }
  .front__divider {
    position: absolute; left: 288px; top: 74px; width: 1.5px; height: 209px;
    background: var(--rule);
  }
  .front__details { position: absolute; left: 311px; top: 112px; }
  .person__name {
    font-family: "Oswald", sans-serif; font-weight: 700;
    font-size: 31px; line-height: 34px; text-transform: uppercase;
    color: var(--navy); letter-spacing: -0.5px;
  }
  .person__title {
    font-family: "Poppins", sans-serif; font-size: 17px; line-height: 20px;
    color: var(--ink);
  }
  .contact { list-style: none; margin-top: 18px; }
  .contact__item {
    display: flex; align-items: center; gap: 7px;
    font-family: "Poppins", sans-serif; font-size: 14.5px; line-height: 24px;
    color: var(--ink); white-space: nowrap;
  }
  .contact__icon { width: 16px; height: 16px; flex: none; }

  .back__company {
    position: absolute; left: 0; right: 0; top: 116px;
    font-family: "Oswald", sans-serif; font-weight: 700;
    font-size: 56px; line-height: 62px; text-align: center;
    text-transform: uppercase; color: var(--royal); letter-spacing: -1.2px;
    white-space: nowrap;
  }
</style>
</head>
<body>
<main class="canvas">
  <section class="card card--front" aria-label="Business card front">
    <h1 class="front__company">TK Verdane<br>Consulting LLC</h1>
    <div class="front__divider"></div>
    <div class="front__details">
      <p class="person__name">Delia Hartwig</p>
      <p class="person__title">President</p>
      <ul class="contact">
        <li class="contact__item">
          <svg class="contact__icon" viewBox="0 0 24 24" aria-hidden="true">
            <path fill="var(--navy)" d="M6.6 10.8a15.2 15.2 0 0 0 6.6 6.6l2.2-2.2c.3-.3.7-.4 1-.2 1.1.4 2.3.6 3.6.6.6 0 1 .4 1 1V20c0 .6-.4 1-1 1A17 17 0 0 1 3 4c0-.6.4-1 1-1h3.5c.6 0 1 .4 1 1 0 1.3.2 2.5.6 3.6.1.3 0 .7-.2 1z"/>
            <path fill="none" stroke="var(--navy)" stroke-width="1.8" d="M14 3.5a7 7 0 0 1 6.5 6.5M14 7a3.5 3.5 0 0 1 3 3"/>
          </svg>
          <span>555-862-4197</span>
        </li>
        <li class="contact__item">
          <svg class="contact__icon" viewBox="0 0 24 24" aria-hidden="true">
            <rect x="1" y="5" width="22" height="14" fill="var(--navy)"/>
            <path fill="none" stroke="#ffffff" stroke-width="1.4" d="M1 5l11 8 11-8M1 19l8-7M23 19l-8-7"/>
          </svg>
          <span>hartwigdl47@mailnest.example</span>
        </li>
      </ul>
    </div>
    <div class="front__band"></div>
  </section>

  <section class="card card--back" aria-label="Business card back">
    <p class="back__company">TK Verdane<br>Consulting LLC</p>
  </section>
</main>
</body>
</html>
```